Business card design needed

I am a nutritionist and fitness instructor and I need a business card designed for my company SowGrowThrive. I provide nutrition education services such as consultations, cooking demonstrations, workshops, and supermarket tours. I also provide fitness instruction and training to clients to help overhaul their lifestyle.

I would like to see designs that have a natural, organic, feel using earthy colours. I would like to have cards printed on recycled paper.

I would prefer a 2 sided card. Front side with just the business name Sow Grow Thrive and underneath Nutrition Health Fitness. The second side to have the contact details.

The final design should communicate health and wellness through eating organic wholefoods and being physically active.

Although I have this idea, I would be open to see other suggestions that have a similar look and feel.
Updates

Target Market(s)

people interested in being healthier, women wanting to loose weight, mothers wanting to be healthier for their families

Industry/Entity Type

Nutrition

Contact Information for Business Card

Nadia Crewe
Nutritionist and Personal Trainer
M 0417582936
E sowgrowthrivenutrition@mailbox-example.net

Logo Text

SowGrowThrive (underneath) Nutrition Health Fitness

Logo styles of interest
Wordmark Logo
Requirements
Nice to have
• I like the idea of having the letters of SowGrowThrive spelt out with food such as grains, nuts, seeds, legumes, fruit etc. For example close up images of cherry tomatoes, chia seeds, kidney beans, chickpeas, blue berries, raspberries, brown rice - lots of different colours and textures. Continuing playing on the idea of the book cover Dig Rest Glow.

food is important - I am not selling supplements rather I am promoting the enjoyment of healthy wholefoods so food is important to the look and feel of the design
Should not have
• cartoon images
images associated with body building or supplements
fruit or dumb bells with tape measures around them
clichés for weight loss such as scales and tape measures
I don't want to look like other typical wellness services such as massage or spa services

```html
<!DOCTYPE html>
<html lang="en">
<head>
<meta charset="utf-8">
<title>Sow Grow Thrive – Business Card</title>
<link rel="stylesheet" href="https://fonts.googleapis.com/css2?family=Josefin+Sans:wght@300;400&display=swap">
<style>
  :root {
    --backdrop: #e6e6e2;
    --card: #f3f8f4;
    --leaf: #86b04a;
    --grain: #b38c3e;
    --ink: #6f6f6f;
    --tag-nutrition: #c9cf3a;
    --tag-health: #e0763a;
    --tag-fitness: #b0388c;
    --white: #ffffff;
  }
  * { margin: 0; padding: 0; box-sizing: border-box; }
  html, body {
    width: 1200px;
    height: 1000px;
    overflow: hidden;
    background: var(--backdrop);
    font-family: "Josefin Sans", sans-serif;
  }
  .sheet {
    position: relative;
    width: 1200px;
    height: 1000px;
  }
  .card {
    position: absolute;
    left: 220px;
    width: 760px;
    height: 412px;
    background: var(--card);
    box-shadow: 0 6px 18px rgba(0, 0, 0, 0.18);
  }
  .card--front { top: 70px; }
  .card--back { top: 518px; }

  /* Front */
  .wordmark {
    position: absolute;
    left: 0;
    right: 0;
    top: 150px;
    text-align: center;
  }
  .wordmark__name {
    font-weight: 300;
    font-size: 76px;
    letter-spacing: 1px;
    color: var(--grain);
    line-height: 1;
  }
  .wordmark__tagline {
    margin-top: 18px;
    font-weight: 400;
    font-size: 15px;
    letter-spacing: 1px;
  }
  .tag--nutrition { color: var(--tag-nutrition); }
  .tag--health { color: var(--tag-health); }
  .tag--fitness { color: var(--tag-fitness); }

  /* Back */
  .name-band {
    position: absolute;
    left: 0;
    top: 174px;
    width: 381px;
    height: 66px;
    background: var(--leaf);
    color: var(--white);
    padding: 6px 0 0 44px;
  }
  .name-band__name {
    font-weight: 300;
    font-size: 42px;
    letter-spacing: 5px;
    line-height: 1;
  }
  .name-band__role {
    font-weight: 300;
    font-size: 15px;
    line-height: 1.1;
  }
  .contact {
    position: absolute;
    left: 406px;
    top: 180px;
    font-weight: 300;
    font-size: 15px;
    color: var(--ink);
    list-style: none;
  }
  .contact li { margin-bottom: 15px; }
  .contact__label { color: var(--leaf); margin-right: 5px; }
  .mini-mark {
    position: absolute;
    right: 32px;
    bottom: 40px;
    font-weight: 300;
    font-size: 26px;
    color: var(--grain);
  }
</style>
</head>
<body>
  <main class="sheet">
    <section class="card card--front" aria-label="Card front">
      <div class="wordmark">
        <p class="wordmark__name">SowGrowThrive</p>
        <p class="wordmark__tagline">
          <span class="tag--nutrition">NUTRITION</span>
          <span class="tag--health">HEALTH</span>
          <span class="tag--fitness">FITNESS</span>
        </p>
      </div>
    </section>

    <section class="card card--back" aria-label="Card back">
      <div class="name-band">
        <p class="name-band__name">NadiaCrewe</p>
        <p class="name-band__role">Nutritionist and Personal Trainer</p>
      </div>
      <ul class="contact">
        <li><span class="contact__label">m:</span>0417582936</li>
        <li><span class="contact__label">e:</span>sowgrowthrivenutrition@mailbox-example.net</li>
      </ul>
      <p class="mini-mark">SowGrowThrive</p>
    </section>
  </main>
</body>
</html>
```